Need a website setup for our new removalist business.
Our business is called Pine Harbour Removals and would like a website setup.
We don’t have a website, logo or design as of yet. Our truck is blue so something possibly that works and can incorporate the blue.

```html
<!DOCTYPE html>
<html lang="en">
<head>
<meta charset="utf-8">
<title>Pine Harbour Removals — Moving Made Easy</title>
<link href="https://fonts.googleapis.com/css2?family=Krona+One&family=Roboto:wght@400;500;700&display=swap" rel="stylesheet">
<style>
:root{
  --blue:#4a69ad;
  --blue-dark:#3d5a99;
  --ink:#222326;
  --grey-text:#6f6f73;
  --light-grey:#a6a6a8;
  --panel:#f2f2f2;
  --footer:#2f2f30;
  --footer-deep:#262627;
  --bar:#2b2b2c;
  --white:#ffffff;
}
*{margin:0;padding:0;box-sizing:border-box}
html,body{width:1200px;height:3839px;overflow:hidden}
body{position:relative;background:var(--white);font-family:"Roboto",Arial,sans-serif;color:var(--ink)}
.abs{position:absolute}
.display{font-family:"Krona One","Arial Black",sans-serif;font-weight:400;letter-spacing:1px;line-height:1}
.eyebrow{font-weight:500;color:var(--blue);font-size:21px;text-transform:uppercase}
.muted{color:var(--light-grey)}
.btn{position:absolute;display:flex;align-items:center;justify-content:center;background:var(--blue);color:var(--white);font-weight:700;font-size:16px;text-transform:uppercase}
.rule{position:absolute;height:2px;background:var(--blue)}

/* header */
.site-header{position:absolute;left:0;top:0;width:1200px;height:143px;background:var(--white);z-index:3}
.topbar-text{position:absolute;top:12px;color:var(--white);font-size:14px;display:flex;align-items:center;gap:10px}
.brand{position:absolute;left:110px;top:32px;display:flex;align-items:center;gap:12px;z-index:5}
.brand-mark{width:30px;height:30px;background:var(--blue)}
.brand-name{font-weight:700;font-size:19px;line-height:1.2;color:var(--ink);text-transform:uppercase}
.nav a{position:absolute;top:84px;font-size:15px;font-weight:500;color:var(--ink);text-decoration:none}
.nav a.active{color:var(--blue);text-decoration:underline;text-underline-offset:4px}

/* hero */
.hero{position:absolute;left:0;top:143px;width:1200px;height:690px;overflow:hidden}
.hero-photo{position:absolute;inset:0;background:linear-gradient(90deg,#6f6862 0%,#5f6169 35%,#48546a 62%,#34425b 100%)}
.hero-photo::after{content:"";position:absolute;inset:0;background:linear-gradient(90deg,rgba(20,24,32,.45) 0%,rgba(20,24,32,.15) 55%,rgba(0,0,0,0) 100%)}
.hero-copy{position:absolute;left:110px;color:var(--white)}
.dot{position:absolute;left:1139px;width:14px;height:14px;border:2px solid var(--white);border-radius:50%}
.dot.on{background:var(--white)}

/* about */
.about-photo{position:absolute;left:110px;top:866px;width:447px;height:402px;background:linear-gradient(135deg,#b9a08a 0%,#d8c2a8 45%,#c9a983 100%);box-shadow:0 10px 30px rgba(0,0,0,.14)}
.body-copy{position:absolute;font-size:16.5px;line-height:26px;color:var(--grey-text)}

/* services */
.services{position:absolute;left:0;top:1397px;width:1200px;height:966px;background:var(--panel)}
.card-img{position:absolute;width:313px;height:254px}
.card-box{position:absolute;width:270px;height:139px;background:var(--white);padding:20px 22px 0 24px;box-shadow:0 6px 18px rgba(0,0,0,.06)}
.card-box h3{font-size:18px;font-weight:500;color:var(--ink);text-transform:uppercase;margin-bottom:8px}
.card-box p{font-size:13.5px;line-height:22px;color:var(--grey-text)}
.card-box span{display:block;margin-top:6px;font-size:12px;font-weight:700;color:var(--blue)}

/* contact */
.contact{position:absolute;left:0;top:3016px;width:1200px;height:472px;background:linear-gradient(180deg,#4d6cae 0%,#4767a9 100%)}
.field{position:absolute;background:var(--white);border-radius:3px;font-size:15px;color:#555;padding:0 17px;display:flex;align-items:center}

/* footer */
.footer{position:absolute;left:0;top:3488px;width:1200px;height:298px;background:var(--footer);color:var(--white)}
.footer h4{position:absolute;top:58px;font-size:18px;font-weight:500;text-transform:uppercase}
.flink{position:absolute;font-size:14px;display:flex;align-items:center}
.flink i{width:11px;height:11px;border-radius:50%;background:var(--blue);margin-right:14px;display:inline-block}
.finfo{position:absolute;left:902px;font-size:12px;line-height:21px}
.finfo b{font-size:14px;font-weight:500;text-transform:uppercase}
.bottombar{position:absolute;left:0;top:3786px;width:1200px;height:53px;background:var(--footer-deep);color:var(--white);font-size:12.5px}
.social{position:absolute;top:12px;width:31px;height:31px;border:1px solid #d0d0d0}
</style>
</head>
<body>

<header class="site-header">
  <svg class="abs" style="left:0;top:0" width="1200" height="42" aria-hidden="true"><polygon points="611,0 1200,0 1200,42 648,42" fill="#2b2b2c"/></svg>
  <div class="topbar-text" style="left:671px">
    <svg width="13" height="13" viewBox="0 0 24 24"><path d="M6.6 10.8a15 15 0 006.6 6.6l2.2-2.2a1 1 0 011-.25 11.4 11.4 0 003.6.57 1 1 0 011 1V20a1 1 0 01-1 1A17 17 0 013 4a1 1 0 011-1h3.5a1 1 0 011 1 11.4 11.4 0 00.57 3.6 1 1 0 01-.25 1z" fill="#6d8cc9"/></svg>
    +1 (555) 014 2290 <span style="margin-left:8px">|</span>
  </div>
  <div class="topbar-text" style="left:843px">
    <svg width="15" height="12" viewBox="0 0 24 18"><rect width="24" height="18" rx="2" fill="#6d8cc9"/><path d="M1 2l11 8 11-8" stroke="#2b2b2c" stroke-width="2" fill="none"/></svg>
    hello@pineharbourremovals.com
  </div>
  <nav class="nav">
    <a class="active" style="left:411px">HOME</a>
    <a style="left:487px">ABOUT US</a>
    <a style="left:591px">OUR SERVICES &#9662;</a>
    <a style="left:744px">BLOG</a>
    <a style="left:814px">CONTACT US</a>
  </nav>
  <div class="btn" style="left:942px;top:67px;width:146px;height:51px">Get a Quote</div>
</header>

<svg class="abs" style="left:0;top:143px;z-index:4" width="320" height="32" aria-hidden="true"><polygon points="96,0 306,0 290,30 118,30" fill="#fff"/></svg>
<div class="brand">
  <div class="brand-mark"></div>
  <div class="brand-name">Pine Harbour<br>Removals</div>
</div>

<section class="hero">
  <div class="hero-photo" role="img" aria-label="Smiling removalist in cap and work jacket standing in front of a blue moving van"></div>
  <div class="hero-copy" style="top:168px;font-size:21px;font-weight:500">PINE HARBOUR REMOVALS</div>
  <div class="hero-copy display" style="top:205px;font-size:40px">MOVING MADE EASY</div>
  <div class="abs" style="left:110px;top:252px;width:94px;height:2px;background:#fff"></div>
  <div class="hero-copy" style="top:274px;font-size:20.5px;line-height:30px">Lorem ipsum dolor sit amet, consectetur adipiscing elit,<br>sed do eiusmod incididunt ut laborea.</div>
  <div class="btn" style="left:110px;top:359px;width:155px;height:51px">Get Started</div>
  <div class="dot" style="top:255px"></div>
  <div class="dot on" style="top:281px"></div>
  <div class="dot" style="top:306px"></div>
  <div class="dot" style="top:330px"></div>
  <svg class="abs" style="left:0;top:0" width="1200" height="690" aria-hidden="true">
    <polygon points="0,672 303,514 313,528 1200,684 1200,690 0,690" fill="#fff"/>
    <polygon points="303,514 1200,647 1200,686 313,528" fill="#4a69ad"/>
  </svg>
</section>

<div class="about-photo" role="img" aria-label="Happy family unpacking moving boxes in a bright new home"></div>
<div class="abs eyebrow" style="left:629px;top:883px">About Us</div>
<div class="abs display" style="left:629px;top:921px;font-size:35px">WHO <span class="muted">WE ARE</span></div>
<div class="rule" style="left:599px;top:964px;width:57px"></div>
<p class="body-copy" style="left:629px;top:997px;width:472px">Sed ut perspiciatis unde omnis iste natus error sit voluptatem accusantium doloremque laudantium, totam rem aperiam, eaque ipsa quae ab illo inventore veritatis et quasi architecto beatae vitae dicta sunt explicabo.</p>
<p class="body-copy" style="left:629px;top:1115px;width:472px">Nemo enim ipsam voluptatem quia voluptas sit aspernatur aut odit aut fugit, sed quia consequuntur.</p>
<div class="btn" style="left:629px;top:1197px;width:142px;height:52px">Read More</div>

<section class="services"></section>
<div class="abs eyebrow" style="left:0;width:1200px;text-align:center;top:1473px;font-size:19px">Our Services</div>
<div class="abs display" style="left:0;width:1200px;text-align:center;top:1506px;font-size:35px">WHAT <span class="muted">WE DO</span></div>
<div class="rule" style="left:571px;top:1548px;width:57px"></div>

<div class="card-img" style="left:110px;top:1597px;background:linear-gradient(135deg,#d9d3c9,#b99a78)" role="img" aria-label="Movers carrying and packing cardboard boxes"></div>
<div class="card-img" style="left:444px;top:1597px;background:linear-gradient(135deg,#c98f52,#e9c89c)" role="img" aria-label="Family carrying boxes into a sunlit room"></div>
<div class="card-img" style="left:777px;top:1597px;background:linear-gradient(135deg,#e6e4e0,#c7a77f)" role="img" aria-label="Small dog sitting among stacked moving boxes"></div>
<div class="card-img" style="left:110px;top:1961px;background:linear-gradient(135deg,#e3e6e4,#a9a58d)" role="img" aria-label="Office with desks and plants being packed up"></div>
<div class="card-img" style="left:444px;top:1961px;background:linear-gradient(135deg,#ecebe8,#c8a57c)" role="img" aria-label="Open cardboard boxes beside a potted plant"></div>
<div class="card-img" style="left:777px;top:1961px;background:linear-gradient(135deg,#9b9a84,#cfc5b3)" role="img" aria-label="Movers carrying furniture outside a house"></div>

<div class="card-box" style="left:133px;top:1781px"><h3>Packing Services</h3><p>Excepteur sint occaecat cupidatat<br>non proident, sunt in culpa</p><span>VIEW DETAILS</span></div>
<div class="card-box" style="left:466px;top:1781px"><h3>Storage Solutions</h3><p>Excepteur sint occaecat cupidatat<br>non proident, sunt in culpa</p><span>VIEW DETAILS</span></div>
<div class="card-box" style="left:799px;top:1781px"><h3>Specialty Item Moving</h3><p>Excepteur sint occaecat cupidatat<br>non proident, sunt in culpa</p><span>VIEW DETAILS</span></div>
<div class="card-box" style="left:133px;top:2145px"><h3>Office Relocations</h3><p>Excepteur sint occaecat cupidatat<br>non proident, sunt in culpa</p><span>VIEW DETAILS</span></div>
<div class="card-box" style="left:466px;top:2145px"><h3>Local Moving</h3><p>Excepteur sint occaecat cupidatat<br>non proident, sunt in culpa</p><span>VIEW DETAILS</span></div>
<div class="card-box" style="left:799px;top:2145px"><h3>Residential</h3><p>Excepteur sint occaecat cupidatat<br>non proident, sunt in culpa</p><span>VIEW DETAILS</span></div>

<div class="abs eyebrow" style="left:136px;top:2487px;font-size:19px">Pine Harbour Removals</div>
<div class="abs display" style="left:136px;top:2520px;font-size:31px;line-height:37px">SAFE, TRUSTED<br><span class="muted">MOVING</span></div>
<div class="rule" style="left:110px;top:2597px;width:45px"></div>
<p class="body-copy" style="left:137px;top:2622px;width:403px;font-size:15.5px;line-height:25.6px;text-align:justify;color:#444">Sed ut perspiciatis unde omnis iste natus error sit voluptatem accusantium doloremque laudantium, totam rem aperiam, eaque ipsa quae ab illo inventore veritatis et quasi architecto beatae vitae dicta sunt explicabo. Nemo enim ipsam voluptatem quia voluptas sit aspernatur aut odit aut fugit, sed quia consequuntur magni dolores eos qui ratione voluptatem sequi nesciunt.</p>
<div class="btn" style="left:137px;top:2832px;width:148px;height:51px">Contact Us</div>
<div class="abs" style="left:827px;top:2477px;width:261px;height:421px;background:#a8a8a8"></div>
<div class="abs" style="left:595px;top:2516px;width:454px;height:342px;background:linear-gradient(135deg,#e7e5e1 0%,#b8a995 55%,#8f7d6a 100%)" role="img" aria-label="Family sitting on the floor under a cardboard roof in their new living room"></div>

<section class="contact" role="region" aria-label="Contact form"></section>
<div class="abs" style="left:0;width:1200px;text-align:center;top:3084px;color:#fff;font-size:19px;font-weight:500">CONTACT US</div>
<div class="abs display" style="left:0;width:1200px;text-align:center;top:3113px;color:#fff;font-size:36px">GET IN TOUCH</div>
<div class="abs" style="left:596px;top:3157px;width:60px;height:2px;background:#fff"></div>
<div class="field" style="left:165px;top:3196px;width:282px;height:49px">Full Name</div>
<div class="field" style="left:459px;top:3196px;width:282px;height:49px">Phone</div>
<div class="field" style="left:751px;top:3196px;width:283px;height:49px">Email Address</div>
<div class="field" style="left:165px;top:3259px;width:869px;height:92px;align-items:flex-start;padding-top:14px">Message</div>
<div class="btn" style="left:519px;top:3367px;width:162px;height:50px;background:#2b2b2c">Send Message</div>

<footer class="footer">
  <div class="abs" style="left:112px;top:104px;display:flex;align-items:center;gap:14px">
    <div style="width:34px;height:34px;background:var(--blue)"></div>
    <div style="font-weight:700;font-size:22px;line-height:1.2;color:#fff">PINE HARBOUR<br>REMOVALS</div>
  </div>
  <h4 style="left:422px">Quick Links</h4>
  <div class="flink" style="left:424px;top:97px"><i></i>Home</div>
  <div class="flink" style="left:424px;top:133px"><i></i>About Us</div>
  <div class="flink" style="left:424px;top:170px"><i></i>Our Services</div>
  <div class="flink" style="left:424px;top:206px"><i></i>Blog</div>
  <div class="flink" style="left:424px;top:242px"><i></i>Contact Us</div>
  <div class="flink" style="left:631px;top:97px"><i></i>Site Map</div>
  <div class="flink" style="left:631px;top:133px"><i></i>Disclaimer</div>
  <div class="flink" style="left:631px;top:170px"><i></i>Privacy Policy</div>
  <div class="flink" style="left:631px;top:206px"><i></i>Terms Of Use</div>
  <h4 style="left:865px">Contact Info</h4>
  <svg class="abs" style="left:865px;top:98px" width="11" height="15" viewBox="0 0 12 16"><path d="M6 0a6 6 0 016 6c0 4-6 10-6 10S0 10 0 6a6 6 0 016-6z" fill="#4a69ad"/><circle cx="6" cy="6" r="2" fill="#2f2f30"/></svg>
  <div class="finfo" style="top:95px"><b>Address:</b><br>12 Wharf Lane, Harbourside,<br>Australia</div>
  <svg class="abs" style="left:865px;top:174px" width="13" height="13" viewBox="0 0 24 24"><path d="M6.6 10.8a15 15 0 006.6 6.6l2.2-2.2a1 1 0 011-.25 11.4 11.4 0 003.6.57 1 1 0 011 1V20a1 1 0 01-1 1A17 17 0 013 4a1 1 0 011-1h3.5a1 1 0 011 1 11.4 11.4 0 00.57 3.6 1 1 0 01-.25 1z" fill="#4a69ad"/></svg>
  <div class="finfo" style="top:171px"><b>Phone:</b><br>+1 (555) 014 2290</div>
  <svg class="abs" style="left:865px;top:229px" width="15" height="11" viewBox="0 0 24 18"><rect width="24" height="18" rx="2" fill="#4a69ad"/><path d="M1 2l11 8 11-8" stroke="#2f2f30" stroke-width="2" fill="none"/></svg>
  <div class="finfo" style="top:224px"><b>Email:</b><br>hello@pineharbourremovals.com</div>
</footer>
<div class="bottombar">
  <div class="abs" style="left:0;width:1200px;text-align:center;top:19px">© 2024 PINE HARBOUR REMOVALS &nbsp;|&nbsp; All Rights Reserved</div>
  <div class="social" style="left:977px;background:var(--blue);border-color:var(--blue)" aria-label="Social profile"></div>
  <div class="social" style="left:1017px" aria-label="Social profile"></div>
  <div class="social" style="left:1056px" aria-label="Social profile"></div>
</div>

</body>
</html>
```